Pasta Sauce Label for Kestrel Sauce

We need a label for our pasta sauce. We already have a logo and business card designs that i can attach for inspiration and consistency. Looking to use neutral colors, beiges, whites, plus our main color green. you can also see some of our design elements on our website. www.thekestrelsauce-example.com
Also we need space to put nutrition labels and UPC codes as well. I don't have the information for those just yet.
The label will be printed on recycled wood or other material. So the background not being a specific color would be helpful in making it "pop".
Thanks!
Food Production

```html
<!DOCTYPE html>
<html lang="en">
<head>
<meta charset="utf-8">
<title>Kestrel Sauce – Pasta Sauce Label</title>
<link rel="stylesheet" href="https://fonts.googleapis.com/css2?family=Anton&family=Allura&family=Montserrat:wght@400&display=swap">
<style>
  :root {
    --page: #f3f2ef;
    --label-cream: #f6f3e6;
    --brand-green: #2fa84f;
    --ink: #1d1c1b;
    --tomato-red: #e0404a;
    --tomato-pink: #ef5c68;
    --rule: #2a2a2a;
  }
  * { box-sizing: border-box; margin: 0; padding: 0; }
  html, body {
    width: 1090px; height: 1200px; overflow: hidden;
    background: var(--page);
  }
  .canvas { position: relative; width: 1090px; height: 1200px; }

  .label {
    position: absolute; left: 95px; top: 120px;
    width: 900px; height: 960px;
    background: var(--label-cream);
    overflow: hidden;
  }
  .label__band {
    position: absolute; left: 0; width: 100%; height: 40px;
    background: var(--brand-green);
  }
  .label__band--top { top: 0; }
  .label__band--bottom { bottom: 0; }

  .brand {
    position: absolute; left: 44px; top: 110px;
    display: flex; align-items: center; gap: 14px;
    font-family: "Montserrat", sans-serif; font-weight: 400;
    font-size: 34px; color: var(--brand-green);
    text-transform: uppercase; letter-spacing: 1px;
  }
  .brand__dot {
    width: 34px; height: 34px; border-radius: 50%;
    background: var(--brand-green);
  }

  .speed-lines { position: absolute; left: 390px; top: 150px; }

  .title {
    position: absolute; left: 70px; top: 290px; width: 700px;
    font-family: "Anton", sans-serif; color: var(--ink);
    text-transform: uppercase; line-height: 0.95;
    transform: skewX(-10deg);
  }
  .title__line {
    display: block; font-size: 190px; letter-spacing: 4px;
    text-shadow: -6px 6px 0 var(--label-cream), -10px 10px 0 var(--tomato-red);
  }
  .title__line--first { padding-left: 40px; }

  .variety {
    position: absolute; left: 60px; top: 740px; width: 400px; height: 130px;
  }
  .variety__name {
    position: absolute; left: 70px; top: 18px;
    font-family: "Allura", cursive; font-size: 82px; color: var(--ink);
  }
  .variety__rule {
    position: absolute; height: 3px; background: var(--rule);
  }
  .variety__rule--top { left: 130px; top: 22px; width: 230px; }
  .variety__rule--bottom { left: 0; top: 110px; width: 240px; }

  .tomatoes {
    position: absolute; left: 514px; top: 676px; width: 260px; height: 228px;
    border-radius: 110px;
    background: radial-gradient(circle at 40% 50%, var(--tomato-pink), var(--tomato-red));
  }
</style>
</head>
<body>
<main class="canvas">
  <section class="label">
    <div class="label__band label__band--top"></div>

    <div class="brand">
      <span class="brand__dot"></span>
      <span class="brand__name">Kestrel Sauce</span>
    </div>

    <svg class="speed-lines" width="320" height="60" viewBox="0 0 320 60">
      <g stroke="#1d1c1b" stroke-width="3" stroke-linecap="round">
        <line x1="0" y1="8" x2="110" y2="8"/>
        <line x1="140" y1="8" x2="260" y2="8"/>
        <line x1="30" y1="30" x2="90" y2="30"/>
        <line x1="60" y1="52" x2="300" y2="52"/>
      </g>
    </svg>

    <h1 class="title">
      <span class="title__line title__line--first">Pasta</span>
      <span class="title__line">Sauce</span>
    </h1>

    <div class="variety">
      <span class="variety__rule variety__rule--top"></span>
      <span class="variety__name">Bolognese</span>
      <span class="variety__rule variety__rule--bottom"></span>
    </div>

    <div class="tomatoes" role="img" aria-label="Illustration of two ripe tomatoes"></div>

    <div class="label__band label__band--bottom"></div>
  </section>
</main>
</body>
</html>
```